New Signage Design Project for Qb Dale Outworks *

Im Looking for yard design with our logo, number, website, services & credentials. Each Yard sign will be for 3 different titles...

Example 1: New Roof Coming Soon (Title) This Yardsign is for projects before we start them... Letting neighbors know why we are going to be there.
Example 2: New Roof In progress (Title) This Yardsign is for during the process of the work.. letting neighbors know what we working on!!
Example 3: This Design is only for the customer that says a title NEW ROOF INSTALL SATISFIED CUSTOMER ON THIS DESIGN I DONT NEED SERVICES JSUT LOGO AND THE TITLE

Target Market(s)

Customers

Industry/Entity Type

Roofing

Font styles to use
Serif
Sans Serif

Colors
33b8a4
5c5c5c

Requirements
Must have
• -LOGO
• -WEBSITE
• -NUMBER
• -TITLES
• -SERVICES (ROOFING, GUTTERS, PAINTING, PRESSURE WASHING, EXTERIOR DESIGN.)
• -CREDENTIALS
• -HOUSE SHAPE DESIGN
• -LOGO COLORS
• -NOT BUSY BUT CLEAN AND SHARP
• -MATTE COLORS
Nice to have
• Easy To read, Eye Catchy, Clean Design, logo colors, titles
Should not have
• not Busy,

```html
<!DOCTYPE html>
<html lang="en">
<head>
<meta charset="utf-8">
<title>Qb Dale Outworks – New Roof Coming Soon Yard Sign</title>
<link href="https://fonts.googleapis.com/css2?family=Oswald:wght@400;500;600;700&family=Roboto+Condensed:wght@700&family=Cormorant+Garamond:wght@600&display=swap" rel="stylesheet">
<style>
  :root{
    --teal:#33b8a4;
    --charcoal:#484848;
    --charcoal-dark:#3d3d3d;
    --white:#ffffff;
    --backdrop:#9b9b9b;
    --badge-blue:#1f5fa8;
    --badge-red:#c8322d;
  }
  *{margin:0;padding:0;box-sizing:border-box;}
  html,body{width:800px;height:1200px;overflow:hidden;}
  body{background:var(--backdrop);position:relative;font-family:"Oswald",sans-serif;}
  .yard-sign{position:absolute;left:246px;top:25px;width:308px;height:1150px;background:var(--charcoal);overflow:hidden;}
  .sign-shapes{position:absolute;inset:0;width:100%;height:100%;}
  .brand{position:absolute;top:110px;left:0;width:100%;text-align:center;color:var(--white);}
  .brand-mark{display:inline-block;width:26px;height:26px;border:3px solid var(--white);margin-bottom:8px;}
  .brand-name{font-family:"Cormorant Garamond",serif;font-weight:600;font-size:40px;line-height:1;letter-spacing:2px;text-transform:uppercase;}
  .brand-sub{font-family:"Cormorant Garamond",serif;font-weight:600;font-size:20px;letter-spacing:3px;text-transform:uppercase;margin-top:4px;}
  .brand-tagline{font-family:"Cormorant Garamond",serif;font-weight:600;font-size:11px;letter-spacing:2px;text-transform:uppercase;margin-top:3px;}
  .title-box{position:absolute;top:325px;left:40px;width:228px;height:104px;border:2px solid var(--teal);text-align:center;padding-top:6px;}
  .title-line{font-weight:700;font-size:40px;line-height:44px;color:var(--white);text-transform:uppercase;}
  .title-line .accent{color:var(--teal);}
  .title-line.small{font-size:36px;line-height:42px;}
  .services{position:absolute;top:448px;left:40px;}
  .services-heading{font-weight:700;font-size:33px;color:var(--teal);text-transform:uppercase;letter-spacing:.5px;}
  .service-list{list-style:none;margin-top:22px;}
  .service-list li{font-family:"Roboto Condensed",sans-serif;font-weight:700;font-size:24px;color:var(--white);text-transform:uppercase;line-height:38px;display:flex;align-items:center;}
  .service-list li::before{content:"";width:14px;height:14px;border-radius:50%;background:var(--white);margin-right:18px;}
  .credentials{position:absolute;top:775px;left:40px;display:flex;align-items:center;gap:34px;}
  .credential-a{width:36px;height:50px;background:var(--badge-blue);border-radius:3px;}
  .credential-b{width:82px;height:34px;background:var(--white);border-bottom:8px solid var(--badge-red);border-radius:3px;}
  .contact-cta{position:absolute;top:880px;left:94px;width:120px;height:130px;}
  .cta-text{position:absolute;inset:0;display:flex;flex-direction:column;justify-content:center;align-items:center;color:var(--white);font-weight:700;font-size:20px;line-height:22px;text-transform:uppercase;text-align:center;}
  .contact-phone{position:absolute;top:1028px;width:100%;text-align:center;color:var(--white);font-weight:700;font-size:28px;}
  .contact-web{position:absolute;top:1072px;width:100%;text-align:center;color:var(--white);font-weight:600;font-size:15px;letter-spacing:.3px;}
</style>
</head>
<body>
  <div class="yard-sign">
    <svg class="sign-shapes" viewBox="0 0 308 1150" aria-hidden="true">
      <polygon points="0,0 308,0 308,175 154,60 0,175" fill="var(--teal)"/>
      <polyline points="0,160 154,48 308,160" fill="none" stroke="var(--white)" stroke-width="14"/>
      <polyline points="18,188 154,88 290,188" fill="none" stroke="var(--charcoal-dark)" stroke-width="3"/>
      <polygon points="0,840 154,955 308,840 308,1150 0,1150" fill="var(--teal)"/>
      <polyline points="0,822 154,936 308,822" fill="none" stroke="var(--white)" stroke-width="10"/>
    </svg>

    <header class="brand">
      <span class="brand-mark"></span>
      <div class="brand-name">Qb Dale</div>
      <div class="brand-sub">Outworks</div>
      <div class="brand-tagline">When quality matters</div>
    </header>

    <div class="title-box">
      <div class="title-line">New <span class="accent">Roof</span></div>
      <div class="title-line small">Coming Soon</div>
    </div>

    <section class="services">
      <h2 class="services-heading">Our Services</h2>
      <ul class="service-list">
        <li>Roofing</li>
        <li>Gutters</li>
        <li>Painting</li>
        <li>Pressure Washing</li>
        <li>Exterior Design</li>
      </ul>
    </section>

    <div class="credentials">
      <div class="credential-a"></div>
      <div class="credential-b"></div>
    </div>

    <div class="contact-cta">
      <svg width="120" height="130" viewBox="0 0 120 130" aria-hidden="true">
        <polygon points="60,4 114,34 114,96 60,126 6,96 6,34" fill="var(--teal)" stroke="var(--white)" stroke-width="4"/>
      </svg>
      <div class="cta-text"><span>Get in</span><span>touch</span><span>with us</span></div>
    </div>

    <div class="contact-phone">(503) 555-0142</div>
    <div class="contact-web">www.qbdaleoutworks.com</div>
  </div>
</body>
</html>
```